Vanta-Ride Transit private ambulance flyer/broshure

I need a Tri-fold brochure for our BLS non-emergency private ambulance company. We transport patients to doctors appointments, hyperbarics, dialysis, out of town doctors appointment and scheduled medical procedures etc.

```html
<!DOCTYPE html>
<html lang="en">
<head>
<meta charset="UTF-8">
<title>Vanta-Ride Transit – Non-Emergency Private Ambulance Services</title>
<link rel="stylesheet" href="https://fonts.googleapis.com/css2?family=Montserrat:wght@400;500;600;700&family=Oswald:wght@500;600;700&family=Lexend:wght@400;500&display=swap">
<style>
  :root {
    --green-dark: #1f6a35;
    --green: #2e8b45;
    --green-light: #6fc25a;
    --green-pale: #8fbf97;
    --navy: #2c2f8f;
    --navy-dark: #1f2170;
    --grey-pill: #d6d6d6;
    --ink: #1d1d1d;
    --white: #ffffff;
    --canvas: #e9e9e9;
  }
  * { box-sizing: border-box; margin: 0; padding: 0; }
  html, body { width: 1200px; height: 2325px; overflow: hidden; background: var(--canvas); }
  .flyer {
    position: absolute; left: 40px; top: 370px;
    width: 1120px; height: 1584px;
    background: var(--white);
    box-shadow: 0 4px 18px rgba(0,0,0,.15);
    overflow: hidden;
    font-family: "Montserrat", sans-serif;
    color: var(--ink);
  }
  .hero { position: absolute; left: 0; top: 0; width: 1120px; height: 648px;
    background: linear-gradient(100deg, var(--green-dark) 0%, var(--green) 35%, #5bb26a 48%, var(--green-dark) 75%); }
  .hero-photo { position: absolute; left: 480px; top: 55px; width: 640px; height: 515px;
    background: linear-gradient(120deg, #8c8a86 0%, #c9c6c0 35%, #e8e6e2 55%, #7d7a76 100%); }
  .hero-shapes { position: absolute; left: 0; top: 0; }
  .brand { position: absolute; left: 70px; top: 135px; display: flex; align-items: center; gap: 14px; }
  .brand-mark { width: 34px; height: 34px; background: var(--navy); }
  .brand-name { font-family: "Montserrat", sans-serif; font-weight: 700; font-size: 30px; color: var(--navy); line-height: 1.1; }
  .brand-sub { position: absolute; left: 118px; top: 182px; font-size: 16px; font-weight: 500; color: var(--green-dark); }
  .hero-kicker { position: absolute; left: 56px; top: 330px; font-family: "Lexend", sans-serif; font-weight: 500;
    font-size: 48px; color: var(--white); }
  .hero-title { position: absolute; left: 56px; top: 398px; font-family: "Oswald", sans-serif; font-weight: 600;
    font-size: 72px; line-height: 1; color: var(--white); letter-spacing: -.5px; }
  .hero-title-big { position: absolute; left: 54px; top: 470px; font-family: "Oswald", sans-serif; font-weight: 700;
    font-size: 124px; line-height: 1; color: var(--white); letter-spacing: -1px; }
  .hero-rule { position: absolute; left: 56px; top: 612px; width: 386px; height: 4px; background: var(--white); }
  .hotline { position: absolute; left: 600px; top: 572px; width: 520px; height: 70px;
    background: linear-gradient(90deg, var(--green) 0%, var(--green-dark) 100%);
    clip-path: polygon(4% 0, 100% 0, 100% 100%, 0 100%);
    display: flex; align-items: center; gap: 20px; padding-left: 50px; }
  .hotline-number { font-family: "Oswald", sans-serif; font-weight: 600; font-size: 58px; color: var(--white); line-height: 1; }
  .hero-base { position: absolute; left: 0; top: 650px; width: 1120px; height: 5px; background: var(--green); }

  .section-tag { position: absolute; left: 57px; height: 64px; border-radius: 32px;
    background: var(--green-dark); color: var(--white); font-weight: 600; font-size: 37px;
    display: flex; align-items: center; padding-left: 44px; }
  .section-line { position: absolute; right: 0; height: 3px; background: var(--green-pale); }
  .who-tag { top: 686px; width: 375px; }
  .who-line { top: 717px; left: 432px; }
  .about { position: absolute; left: 80px; right: 50px; top: 768px; font-size: 18.6px; line-height: 1.2;
    text-align: justify; }
  .about p + p { margin-top: 22px; }
  .services-tag { top: 1016px; width: 576px; padding-left: 36px; }
  .services-line { top: 1047px; left: 633px; }

  .service { position: absolute; width: 480px; height: 150px; }
  .service-pill { position: absolute; left: 64px; top: 23px; width: 414px; height: 115px; border-radius: 58px;
    background: var(--grey-pill); }
  .service-divider { position: absolute; left: 175px; top: 38px; width: 3px; height: 86px; background: var(--green-dark); }
  .service-label { position: absolute; left: 198px; top: 23px; height: 115px; width: 270px;
    display: flex; align-items: center; font-weight: 600; font-size: 18px; line-height: 1.25; text-transform: uppercase; }
  .service-badge { position: absolute; left: 0; top: 5px; width: 155px; height: 155px; border-radius: 50%;
    background: var(--navy); border: 6px solid var(--green); box-shadow: inset 0 0 0 3px var(--white);
    display: flex; align-items: center; justify-content: center; }
  .s1 { left: 96px; top: 1100px; } .s2 { left: 596px; top: 1100px; }
  .s3 { left: 96px; top: 1274px; } .s4 { left: 596px; top: 1274px; }

  .contacts { position: absolute; left: 0; top: 1454px; width: 1120px; height: 101px; background: var(--green-dark);
    display: flex; align-items: center; }
  .contact { position: absolute; display: flex; align-items: center; gap: 14px; }
  .contact-icon { width: 56px; height: 56px; border-radius: 50%; background: var(--green-light);
    display: flex; align-items: center; justify-content: center; }
  .contact-label { font-weight: 700; font-size: 30px; color: var(--white); line-height: 1; }
  .contact-number { font-weight: 600; font-size: 22px; color: var(--green-light); line-height: 1.2; }
  .c-office { left: 96px; } .c-fax { left: 410px; } .c-after { left: 716px; }
</style>
</head>
<body>
<main class="flyer">
  <header class="hero">
    <div class="hero-photo" role="img" aria-label="Photo of a white private ambulance driving down a city street with lights on"></div>
    <svg class="hero-shapes" width="1120" height="648" viewBox="0 0 1120 648" aria-hidden="true">
      <defs>
        <linearGradient id="sweep" x1="0" y1="0" x2="1" y2="0">
          <stop offset="0" stop-color="#1f6a35"/><stop offset="1" stop-color="#2e8b45" stop-opacity="0"/>
        </linearGradient>
      </defs>
      <path d="M0 300 C 120 420, 330 320, 480 180 C 560 100, 640 60, 740 55 L 480 55 L 480 648 L 0 648 Z" fill="#2e8b45" opacity=".9"/>
      <path d="M420 648 L 1120 648 L 1120 560 C 900 560, 700 520, 420 648 Z" fill="url(#sweep)"/>
      <path d="M0 0 L 430 0 C 440 170, 370 300, 230 290 C 120 285, 40 250, 0 230 Z" fill="#ffffff"/>
      <path d="M430 0 C 445 180, 370 305, 230 295 C 120 290, 40 255, 0 235" fill="none" stroke="#2e8b45" stroke-width="4"/>
      <path d="M0 0 L 430 0 C 440 170, 370 300, 230 290 C 120 285, 40 250, 0 230 Z" fill="#ffffff"/>
      <rect x="0" y="0" width="1120" height="55" fill="#ffffff"/>
    </svg>
    <div class="brand">
      <span class="brand-mark"></span>
      <span class="brand-name">Vanta-Ride Transit</span>
    </div>
    <div class="brand-sub">Ambulance Services</div>
    <div class="hero-kicker">Non-Emergency</div>
    <div class="hero-title">PRIVATE AMBULANCE</div>
    <div class="hero-title-big">SERVICES</div>
    <div class="hero-rule"></div>
    <div class="hotline">
      <svg width="48" height="48" viewBox="0 0 48 48" aria-hidden="true">
        <circle cx="24" cy="24" r="22" fill="#fff"/>
        <path d="M17 12c2 0 4 5 4 6s-2 2-2 3 4 7 8 8c1 0 2-2 3-2s6 2 6 4-3 5-5 5c-8 0-18-10-18-18 0-3 2-6 4-6z" fill="#1f6a35"/>
      </svg>
      <span class="hotline-number">555-201-7730</span>
    </div>
  </header>
  <div class="hero-base"></div>

  <h2 class="section-tag who-tag">WHO WE ARE</h2>
  <div class="section-line who-line"></div>
  <section class="about">
    <p>Vanta-Ride Transit is a trusted provider of healthcare transportation services, dedicated to ensuring that individuals in our community have access to reliable and compassionate transportation solutions. With years of experience in the industry, we have earned a reputation for excellence in delivering safe, punctual, and personalized transportation to medical appointments, treatments, and specialized care facilities.</p>
    <p>At Vanta-Ride Transit, we understand the importance of each journey, and we are committed to providing the highest level of care to our passengers. Our team of professional drivers and support staff is dedicated to ensuring that every trip is comfortable, stress-free, and tailored to the unique needs of our clients.</p>
  </section>

  <h2 class="section-tag services-tag">SERVICES WE PROVIDE</h2>
  <div class="section-line services-line"></div>

  <div class="service s1">
    <div class="service-pill"></div><div class="service-divider"></div>
    <div class="service-label">BLS Non-Emergency<br>Private Ambulance<br>Services.</div>
    <div class="service-badge">
      <svg width="80" height="60" viewBox="0 0 80 60" aria-hidden="true" fill="#fff">
        <rect x="30" y="10" width="46" height="34" rx="3"/>
        <path d="M6 28 L14 16 H30 V44 H6 Z"/>
        <rect x="49" y="17" width="8" height="20" fill="#2c2f8f"/><rect x="43" y="23" width="20" height="8" fill="#2c2f8f"/>
        <circle cx="18" cy="46" r="7" stroke="#2c2f8f" stroke-width="3"/><circle cx="60" cy="46" r="7" stroke="#2c2f8f" stroke-width="3"/>
        <rect x="36" y="2" width="6" height="6" rx="2"/>
      </svg>
    </div>
  </div>
  <div class="service s2">
    <div class="service-pill"></div><div class="service-divider"></div>
    <div class="service-label">Doctor's Appointments<br>Hyperbaric Treatments<br>Dialysis</div>
    <div class="service-badge">
      <svg width="80" height="70" viewBox="0 0 80 70" aria-hidden="true" fill="none" stroke="#fff" stroke-width="4" stroke-linecap="round">
        <circle cx="18" cy="14" r="7" fill="#fff" stroke="none"/>
        <path d="M24 26 L40 32 L66 32"/>
        <path d="M10 38 H72"/>
        <path d="M22 38 L52 60 M52 38 L22 60"/>
        <circle cx="20" cy="62" r="3" fill="#fff"/><circle cx="54" cy="62" r="3" fill="#fff"/>
      </svg>
    </div>
  </div>
  <div class="service s3">
    <div class="service-pill"></div><div class="service-divider"></div>
    <div class="service-label">Out-of-Town Doctor's<br>Appointments,</div>
    <div class="service-badge">
      <svg width="70" height="72" viewBox="0 0 70 72" aria-hidden="true">
        <path d="M48 16 V28 C48 36 26 32 26 42 C26 52 50 48 50 58 C50 64 40 64 16 64" fill="none" stroke="#fff" stroke-width="4" stroke-linecap="round"/>
        <circle cx="48" cy="12" r="10" fill="#fff"/><text x="48" y="17" font-family="Montserrat, sans-serif" font-size="13" font-weight="700" text-anchor="middle" fill="#2c2f8f">A</text>
        <circle cx="14" cy="40" r="10" fill="#fff"/><text x="14" y="45" font-family="Montserrat, sans-serif" font-size="13" font-weight="700" text-anchor="middle" fill="#2c2f8f">B</text>
        <circle cx="12" cy="64" r="5" fill="#fff"/>
      </svg>
    </div>
  </div>
  <div class="service s4">
    <div class="service-pill"></div><div class="service-divider"></div>
    <div class="service-label">Scheduled Medical<br>Procedures.</div>
    <div class="service-badge">
      <svg width="80" height="70" viewBox="0 0 80 70" aria-hidden="true">
        <path d="M40 44 C20 30 16 22 16 16 C16 8 22 4 28 4 C34 4 38 8 40 12 C42 8 46 4 52 4 C58 4 64 8 64 16 C64 22 60 30 40 44 Z" fill="#fff"/>
        <path d="M20 20 H32 L36 12 L42 28 L46 20 H60" fill="none" stroke="#2c2f8f" stroke-width="3"/>
        <path d="M4 34 L16 54 H34 L38 62 M76 34 L64 54 H46 L42 62" fill="none" stroke="#fff" stroke-width="4" stroke-linecap="round" stroke-linejoin="round"/>
      </svg>
    </div>
  </div>

  <footer class="contacts">
    <div class="contact c-office">
      <span class="contact-icon"><svg width="30" height="30" viewBox="0 0 48 48" aria-hidden="true"><path d="M14 6c3 0 6 8 6 9s-3 3-3 4 6 11 12 12c1 0 3-3 4-3s9 3 9 6-4 8-7 8C22 42 6 26 6 14c0-4 4-8 8-8z" fill="#fff"/></svg></span>
      <div><div class="contact-label">OFFICE</div><div class="contact-number">555-201-7730</div></div>
    </div>
    <div class="contact c-fax">
      <span class="contact-icon"><svg width="30" height="30" viewBox="0 0 48 48" aria-hidden="true"><path d="M14 6c3 0 6 8 6 9s-3 3-3 4 6 11 12 12c1 0 3-3 4-3s9 3 9 6-4 8-7 8C22 42 6 26 6 14c0-4 4-8 8-8z" fill="#fff"/></svg></span>
      <div><div class="contact-label">FAX</div><div class="contact-number">555-201-7731</div></div>
    </div>
    <div class="contact c-after">
      <span class="contact-icon"><svg width="30" height="30" viewBox="0 0 48 48" aria-hidden="true"><path d="M14 6c3 0 6 8 6 9s-3 3-3 4 6 11 12 12c1 0 3-3 4-3s9 3 9 6-4 8-7 8C22 42 6 26 6 14c0-4 4-8 8-8z" fill="#fff"/></svg></span>
      <div><div class="contact-label">AFTER HOURS</div><div class="contact-number">555-201-7732</div></div>
    </div>
  </footer>
</main>
</body>
</html>
```